Higher co-efficient of performance means more heat for your money

I need a bar graph that will have the following heating systems, 80% efficient gas furnace COP of .8, Electric heat COP of 1, and Our best selling heat pump with a cop of 4 at 47F. I will have a constant bar, 100$ worth of gas for furnace, 100$ of electricity for electric heat, and 100$ worth of electricity for our heat pumps. next to them I will have a bar showing how much heat each heating system will provide for $100 of fuel. For gas furnace I need a bar that says $80 worth of heat and the barograph to match it, for electric heat I need the bar to show 100$ worth of heat, for our best selling heat pump I need the bar graph to show and say $400 dollars worth of heat. Please take a look at my website www.summitbreezecomfort.example for brand color and feel

```html
<!DOCTYPE html>
<html lang="en">
<head>
<meta charset="utf-8">
<title>Higher COP Means More Heat For Your Money</title>
<link href="https://fonts.googleapis.com/css2?family=Barlow:wght@400;500;600&display=swap" rel="stylesheet">
<style>
  :root {
    --brand-blue: #1565b0;
    --brand-red: #c8202a;
    --axis-grey: #d6d8d9;
    --rule-grey: #b9bcbe;
    --bubble-blue: #a6dbf6;
    --bg-top: #ffffff;
    --bg-bottom: #eeefef;
  }
  html, body {
    margin: 0;
    padding: 0;
    overflow: hidden;
  }
  .poster {
    position: relative;
    width: 1200px;
    height: 738px;
    overflow: hidden;
    background: linear-gradient(160deg, var(--bg-top) 0%, #f6f7f7 50%, var(--bg-bottom) 100%);
    font-family: "Barlow", Arial, sans-serif;
  }
  .chart {
    position: absolute;
    inset: 0;
  }
  .axis-label {
    font-family: "Barlow", Arial, sans-serif;
    font-size: 31px;
    font-weight: 400;
    fill: var(--axis-grey);
  }
  .bar-label {
    font-family: "Barlow", Arial, sans-serif;
    font-size: 11px;
    font-weight: 500;
    fill: #ffffff;
    letter-spacing: 0.3px;
  }
  .brand {
    position: absolute;
    left: 960px;
    top: 170px;
    width: 170px;
    display: flex;
    flex-direction: column;
    align-items: center;
    gap: 8px;
  }
  .brand-mark {
    width: 44px;
    height: 44px;
    border-radius: 50%;
    background: var(--brand-red);
  }
  .brand-name {
    margin: 0;
    font-size: 20px;
    font-weight: 600;
    color: var(--brand-blue);
    text-align: center;
    line-height: 1.1;
    letter-spacing: 1px;
  }
  .headline-box {
    position: absolute;
    left: 775px;
    top: 322px;
    width: 362px;
    height: 70px;
  }
  .corner {
    position: absolute;
    width: 25px;
    height: 25px;
    border-color: var(--brand-red);
    border-style: solid;
  }
  .corner--top-left { left: 0; top: 0; border-width: 1.5px 0 0 1.5px; }
  .corner--bottom-right { right: 0; bottom: 0; border-width: 0 1.5px 1.5px 0; }
  .headline {
    position: absolute;
    left: 14px;
    top: 7px;
    margin: 0;
    font-size: 17.5px;
    font-weight: 500;
    line-height: 23px;
    color: var(--brand-blue);
    white-space: nowrap;
  }
  .footnote {
    position: absolute;
    left: 14px;
    top: 52px;
    margin: 0;
    font-size: 12.5px;
    font-weight: 500;
    color: var(--brand-blue);
  }
  .legend-item {
    position: absolute;
    left: 790px;
    margin: 0;
    font-size: 16px;
    font-weight: 500;
    color: var(--brand-blue);
    white-space: nowrap;
    transform: translateY(-50%);
  }
</style>
</head>
<body>
<main class="poster">
  <svg class="chart" width="1200" height="738" viewBox="0 0 1200 738" aria-label="Bar chart comparing $100 of fuel with the heat it delivers">
    <defs>
      <linearGradient id="blue-front" x1="0" y1="0" x2="0" y2="1">
        <stop offset="0" stop-color="#6a9ec1"/>
        <stop offset="1" stop-color="#b4dcd8"/>
      </linearGradient>
      <linearGradient id="blue-side" x1="0" y1="0" x2="0" y2="1">
        <stop offset="0" stop-color="#3e7ca6"/>
        <stop offset="1" stop-color="#80cbd2"/>
      </linearGradient>
      <linearGradient id="blue-top" x1="0" y1="0" x2="0" y2="1">
        <stop offset="0" stop-color="#8fc4e0"/>
        <stop offset="1" stop-color="#e3f2f4"/>
      </linearGradient>
      <linearGradient id="red-front" x1="0" y1="0" x2="0" y2="1">
        <stop offset="0" stop-color="#e64d56"/>
        <stop offset="1" stop-color="#c2474f"/>
      </linearGradient>
      <linearGradient id="red-side" x1="0" y1="0" x2="0" y2="1">
        <stop offset="0" stop-color="#e21d26"/>
        <stop offset="1" stop-color="#a41c28"/>
      </linearGradient>
      <linearGradient id="pink-side" x1="0" y1="0" x2="0" y2="1">
        <stop offset="0" stop-color="#e99399"/>
        <stop offset="1" stop-color="#d9646c"/>
      </linearGradient>
      <linearGradient id="ghost-side" x1="0" y1="0" x2="0" y2="1">
        <stop offset="0" stop-color="#f4f4f4"/>
        <stop offset="1" stop-color="#f4f4f4" stop-opacity="0"/>
      </linearGradient>
    </defs>

    <!-- value gridlines -->
    <g class="gridlines" stroke="var(--rule-grey)" stroke-width="1" stroke-dasharray="2 3">
      <line x1="193" y1="267" x2="708" y2="87"/>
      <line x1="193" y1="324" x2="708" y2="143"/>
      <line x1="193" y1="380" x2="708" y2="199"/>
      <line x1="193" y1="436" x2="708" y2="255"/>
      <line x1="193" y1="492" x2="708" y2="311"/>
      <line x1="193" y1="549" x2="708" y2="367"/>
    </g>

    <!-- value axis -->
    <g class="axis-labels">
      <text class="axis-label" transform="translate(127 296) skewY(-18)">$500</text>
      <text class="axis-label" transform="translate(127 354) skewY(-18)">$400</text>
      <text class="axis-label" transform="translate(127 411) skewY(-18)">$300</text>
      <text class="axis-label" transform="translate(127 468) skewY(-18)">$200</text>
      <text class="axis-label" transform="translate(127 525) skewY(-18)">$100</text>
      <text class="axis-label" transform="translate(127 582) skewY(-18)">$0</text>
    </g>

    <!-- ground shadows -->
    <g class="ground-shadow" fill="#000" opacity="0.06">
      <ellipse cx="300" cy="594" rx="42" ry="7"/>
      <ellipse cx="630" cy="492" rx="40" ry="6"/>
    </g>

    <!-- $100 reference outline behind the gas furnace heat bar -->
    <g class="bar bar--reference">
      <polygon points="325,444 363,431 400,444 363,457" fill="#ececec"/>
      <polygon points="325,444 363,457 363,490 325,477" fill="#d7d7d7" opacity="0.7"/>
      <polygon points="363,457 400,444 400,478 363,490" fill="url(#ghost-side)"/>
    </g>

    <!-- gas furnace: $80 of heat -->
    <g class="bar bar--heat-gas">
      <polygon points="325,477 363,490 363,582 325,569" fill="url(#red-front)"/>
      <polygon points="363,490 400,478 400,569 363,582" fill="url(#pink-side)"/>
      <polygon points="325,477 363,465 400,478 363,490" fill="#f1c9cc"/>
      <text class="bar-label" transform="translate(377 572) rotate(-90)">$80 OF HEAT</text>
    </g>

    <!-- gas furnace: $100 of gas -->
    <g class="bar bar--fuel-gas">
      <polygon points="277,461 315,474 315,599 277,586" fill="url(#blue-front)"/>
      <polygon points="315,474 352,461 352,586 315,599" fill="url(#blue-side)"/>
      <polygon points="277,461 315,448 352,461 315,474" fill="url(#blue-top)"/>
      <text class="bar-label" transform="translate(336 587) rotate(-90)">$100 OF GAS</text>
    </g>

    <!-- electric heat: $100 of heat -->
    <g class="bar bar--heat-electric">
      <polygon points="448,400 486,413 486,538 448,525" fill="url(#red-front)"/>
      <polygon points="486,413 524,400 524,525 486,538" fill="url(#pink-side)"/>
      <polygon points="448,400 486,387 524,400 486,413" fill="#e99aa0"/>
      <text class="bar-label" transform="translate(500 528) rotate(-90)">$100 OF HEAT</text>
    </g>

    <!-- electric heat: $100 of electricity -->
    <g class="bar bar--fuel-electric">
      <polygon points="400,417 438,430 438,555 400,542" fill="url(#blue-front)"/>
      <polygon points="438,430 476,418 476,542 438,555" fill="url(#blue-side)"/>
      <polygon points="400,417 438,405 476,418 438,430" fill="url(#blue-top)"/>
      <text class="bar-label" transform="translate(452 545) rotate(-90)">$100 OF ELECTRICITY</text>
    </g>

    <!-- heat pump: $400 of heat -->
    <g class="bar bar--heat-pump">
      <polygon points="572,192 610,205 610,494 572,481" fill="url(#red-front)"/>
      <polygon points="610,205 648,192 648,481 610,494" fill="url(#red-side)"/>
      <polygon points="572,192 610,179 648,192 610,205" fill="#dc5e68"/>
      <text class="bar-label" transform="translate(623 486) rotate(-90)">$400 OF HEAT</text>
    </g>

    <!-- heat pump: $100 of electricity -->
    <g class="bar bar--fuel-pump">
      <polygon points="524,373 562,386 562,511 524,498" fill="url(#blue-front)"/>
      <polygon points="562,386 599,373 599,498 562,511" fill="url(#blue-side)"/>
      <polygon points="524,373 562,360 599,373 562,386" fill="url(#blue-top)"/>
      <text class="bar-label" transform="translate(576 503) rotate(-90)">$100 OF ELECTRICITY</text>
    </g>

    <!-- category icons -->
    <g class="icon-bubble icon-bubble--gas">
      <polygon points="283,383 339,365 339,404 283,422" fill="var(--bubble-blue)"/>
      <polygon points="306,418 316,414 311,423" fill="var(--bubble-blue)"/>
      <path d="M311 409 c-6 -2 -7 -9 -3 -14 c1 3 3 4 4 4 c-1 -5 2 -10 6 -12 c-1 4 2 6 3 9 c2 4 0 10 -5 12 c2 -3 1 -6 -1 -7 c0 3 -2 5 -4 8z" fill="#ffffff"/>
    </g>
    <g class="icon-bubble icon-bubble--electric">
      <polygon points="407,341 463,322 463,361 407,378" fill="var(--bubble-blue)"/>
      <polygon points="430,374 440,371 435,380" fill="var(--bubble-blue)"/>
      <polygon points="441,331 428,353 436,351 426,370 446,344 438,346 447,330" fill="#ffffff"/>
    </g>
    <g class="icon-bubble icon-bubble--heat-pump">
      <polygon points="532,295 588,277 588,316 532,334" fill="var(--bubble-blue)"/>
      <polygon points="555,330 565,327 560,336" fill="var(--bubble-blue)"/>
      <g transform="translate(560 305)" fill="#ffffff">
        <circle r="3.5"/>
        <path d="M0 -4 C4 -14 12 -10 9 -5 C7 -3 3 -3 0 -4z"/>
        <path d="M0 -4 C4 -14 12 -10 9 -5 C7 -3 3 -3 0 -4z" transform="rotate(72)"/>
        <path d="M0 -4 C4 -14 12 -10 9 -5 C7 -3 3 -3 0 -4z" transform="rotate(144)"/>
        <path d="M0 -4 C4 -14 12 -10 9 -5 C7 -3 3 -3 0 -4z" transform="rotate(216)"/>
        <path d="M0 -4 C4 -14 12 -10 9 -5 C7 -3 3 -3 0 -4z" transform="rotate(288)"/>
      </g>
    </g>

    <!-- legend leader lines -->
    <g class="leaders" stroke="var(--rule-grey)" stroke-width="1">
      <line x1="648" y1="497" x2="773" y2="497"/>
      <line x1="534" y1="546" x2="773" y2="546"/>
      <line x1="399" y1="599" x2="773" y2="599"/>
    </g>
    <g class="leader-dots" fill="#9a9d9f">
      <circle cx="648" cy="497" r="2"/>
      <circle cx="534" cy="546" r="2"/>
      <circle cx="399" cy="599" r="2"/>
    </g>
  </svg>

  <div class="brand">
    <span class="brand-mark" aria-hidden="true"></span>
    <p class="brand-name">SUMMIT BREEZE<br>COMFORT</p>
  </div>

  <section class="headline-box">
    <span class="corner corner--top-left"></span>
    <span class="corner corner--bottom-right"></span>
    <h1 class="headline">Higher Co-efficient of Performance (COP)<br>means more heat for your money</h1>
    <p class="footnote">*COP measure at 47°F</p>
  </section>

  <p class="legend-item" style="top:497px">Our Best selling Heat Pump - COP of 4 at 47°F</p>
  <p class="legend-item" style="top:546px">Electric Heat - COP of 1</p>
  <p class="legend-item" style="top:599px">80% Efficient Gas Furnace - COP of .8</p>
</main>
</body>
</html>
```